Healer at the Hearth needs business card

We need a business card that reflects the look and feel of the new website at www.healerathehearth.ca

Our patient navigation and advocacy services are most commonly used by seniors who feel overwhelmed by the health care system and want someone on their side to advocate for their care. Individuals with ill parents or other family members may also come to rely on Healer at the Hearth to help them support their loved one through their health care journey. Ultimately, anyone who finds their health care experience challenging and wants someone completely focused on their needs can benefit from the services of our doctor / nurse team.

Business

Must have
• One design tailored for two clinician which should include: logo, name, title, tel, email, web address and tagline
Nice to have
• A banner image to create a similar look to the website at www.healerathehearth.ca
Should not have
• Too cluttered or busy - must be clean and professional

```html
<!DOCTYPE html>
<html lang="en">
<head>
<meta charset="utf-8">
<title>Healer at the Hearth – Business Card</title>
<link rel="stylesheet" href="https://fonts.googleapis.com/css2?family=PT+Sans:wght@400;700&display=swap">
<style>
  :root {
    --backdrop: #3a3b3d;
    --card: #ffffff;
    --brand-blue: #2f6190;
    --brand-red: #a3212a;
    --rule: #7a7a7a;
    --text-grey: #6b6b6b;
    --text-dark: #2b2b2b;
    --band-light: #e4e4e4;
    --band-mid: #c9c9c9;
  }
  * { box-sizing: border-box; margin: 0; padding: 0; }
  html, body {
    width: 1200px; height: 900px; overflow: hidden;
    background: var(--backdrop);
    font-family: "PT Sans", Arial, sans-serif;
  }
  .canvas { position: relative; width: 1200px; height: 900px; }

  .card {
    position: absolute;
    width: 540px; height: 310px;
    background: var(--card);
    border-radius: 18px;
    overflow: hidden;
    box-shadow: 0 10px 30px rgba(0,0,0,.45);
  }
  .card--contact { left: 90px; top: 120px; }
  .card--front { left: 570px; top: 470px; }

  .wordmark {
    position: absolute;
    display: flex; align-items: center; gap: 12px;
  }
  .wordmark__dot {
    width: 46px; height: 46px; border-radius: 50%;
    background: var(--brand-red); flex: none;
  }
  .wordmark__name {
    color: var(--brand-blue);
    font-size: 30px; line-height: 1.0; font-weight: 400;
  }

  /* contact side */
  .card--contact .wordmark { right: 40px; top: 58px; }
  .card--contact .tagline {
    position: absolute; right: 40px; top: 148px;
    font-size: 11.5px; color: var(--text-grey); letter-spacing: .3px;
  }
  .card--contact .divider {
    position: absolute; left: 0; right: 0; top: 170px;
    height: 3px; background: var(--rule);
  }
  .clinicians {
    position: absolute; left: 32px; top: 186px;
    list-style: none;
    font-size: 12.5px; line-height: 1.35; color: var(--text-dark);
  }
  .clinician + .clinician { margin-top: 8px; }
  .clinician__name { display: block; font-weight: 700; color: var(--brand-blue); }
  .clinician__title { display: block; color: var(--text-grey); font-size: 11.5px; }
  .contact-list {
    position: absolute; right: 40px; top: 186px;
    list-style: none; text-align: right;
    font-size: 12.5px; line-height: 1.45; color: var(--text-dark);
  }

  /* front side */
  .card--front .wordmark { left: 32px; top: 40px; }
  .banner {
    position: absolute; left: 0; right: 0; top: 130px; height: 80px;
    background: linear-gradient(90deg, var(--band-light) 0%, var(--band-light) 45%, var(--band-mid) 75%, #b9b9b9 100%);
  }
  .card--front .divider {
    position: absolute; left: 0; right: 0; top: 210px;
    height: 3px; background: var(--rule);
  }
  .card--front .tagline {
    position: absolute; right: 90px; top: 222px;
    font-size: 14px; color: var(--text-grey);
  }
</style>
</head>
<body>
<main class="canvas">

  <section class="card card--contact" aria-label="Business card, contact side">
    <div class="wordmark">
      <span class="wordmark__dot"></span>
      <span class="wordmark__name">Healer at<br>the Hearth</span>
    </div>
    <p class="tagline">best possible health care for you and your loved ones</p>
    <div class="divider"></div>
    <ul class="clinicians">
      <li class="clinician">
        <span class="clinician__name">Dr. Mara Ellison, MD</span>
        <span class="clinician__title">Physician &amp; Patient Advocate</span>
      </li>
      <li class="clinician">
        <span class="clinician__name">Jonah Pryce, RN</span>
        <span class="clinician__title">Nurse Navigator</span>
      </li>
    </ul>
    <ul class="contact-list">
      <li>Call&nbsp;&nbsp;: 555-014-2290</li>
      <li>email : info@healerathehearth.ca</li>
      <li>Web&nbsp;&nbsp;: www.healerathehearth.ca</li>
    </ul>
  </section>

  <section class="card card--front" aria-label="Business card, front side">
    <div class="wordmark">
      <span class="wordmark__dot"></span>
      <span class="wordmark__name">Healer at<br>the Hearth</span>
    </div>
    <div class="banner" role="img" aria-label="Soft greyscale photo of caring hands resting together"></div>
    <div class="divider"></div>
    <p class="tagline">Health, Love and protection</p>
  </section>

</main>
</body>
</html>
```